New Business and Accounting Software need a Graphics

We need graphic designs for a Business and Accounting Software that has 3 products and several modules.
Each product and module has its owns logo and color, when you do the design have in consideration that we are looking the experience that when you change from one product design to another the look and feel adjust to the color and logo of the product.
I am attaching:
1. Main Logo
2. Logos
3. Word Documents
You are welcome to use other icons for the each product if you want.
Target Market(s)
Independent profesional and Small and Medium Companies
Industry/Entity Type
Business and Accounting Softwares
Look and feel
Each slider illustrates characteristics of the customer's brand and the style your logo design should communicate.

```html
<!DOCTYPE html>
<html lang="es">
<head>
<meta charset="UTF-8">
<title>Nexo Cuentas – Módulos</title>
<link href="https://fonts.googleapis.com/css2?family=Poppins:wght@400;600;700&display=swap" rel="stylesheet">
<style>
  :root{
    --page:#e6e6e6;
    --sheet:#ffffff;
    --gold:#e2b22c;
    --gold-light:#f5e1b0;
    --blue:#1d4f9c;
    --white:#ffffff;
    --icon-a:#c86ec0;
    --icon-b:#e08a3a;
    --icon-c:#6fa8dc;
    --icon-d:#7a7a7a;
    --icon-e:#2aa58a;
    --icon-f:#c9485b;
    --icon-g:#5bb5a6;
    --icon-h:#3b5aa8;
  }
  *{box-sizing:border-box;margin:0;padding:0}
  html,body{width:1200px;height:1000px;overflow:hidden}
  body{background:var(--page);font-family:"Poppins",sans-serif;position:relative}
  .sheet{position:absolute;left:18px;top:88px;width:1164px;height:824px;background:var(--sheet);box-shadow:0 2px 8px rgba(0,0,0,.18);overflow:hidden}
  .decor{position:absolute;left:0;top:0;width:1200px;height:1000px}
  .module{position:absolute;width:191px;height:166px}
  .module svg{position:absolute;left:0;top:0}
  .module-icon{position:absolute;left:50%;top:8px;width:24px;height:24px;margin-left:-12px;border-radius:5px}
  .module-title{position:absolute;left:0;right:0;top:34px;text-align:center;color:var(--blue);font-weight:600;font-size:11.5px;letter-spacing:.3px}
  .module-title.big{font-size:17px;top:29px}
  .module-text{position:absolute;left:22px;right:22px;top:66px;text-align:center;color:var(--white);font-size:9.2px;line-height:1.2;hyphens:auto;-webkit-hyphens:auto}
  .module-text.long{left:26px;right:26px;top:60px;font-size:8.8px;line-height:1.2}
  .brand{position:absolute;left:462px;top:445px;display:flex;align-items:center;gap:14px}
  .brand-dot{width:86px;height:86px;border-radius:50%;background:var(--blue)}
  .brand-name{color:var(--blue);font-weight:700;font-size:34px;line-height:1.05}
</style>
</head>
<body>
<div class="sheet"></div>

<svg class="decor" viewBox="0 0 1200 1000" aria-hidden="true">
  <polygon points="18,88 85,88 148,217 85,346 18,346" fill="var(--gold)"/>
  <polygon points="269,126 312,126 334,164 312,202 269,202 247,164" fill="none" stroke="var(--gold)" stroke-width="5"/>
  <polygon points="354,182 403,182 425,222 403,262 354,262 332,222" fill="var(--gold-light)"/>
  <polygon points="943,145 1080,145 1148,271 1080,398 921,398 960,320 920,253" fill="var(--gold-light)"/>
  <polygon points="843,253 912,253 946,311 912,370 843,370 811,311" fill="var(--gold-light)"/>
  <polygon points="18,551 76,551 108,612 76,672 18,672" fill="none" stroke="var(--gold)" stroke-width="5"/>
  <polygon points="178,605 258,605 300,676 258,748 178,748 136,676" fill="var(--gold-light)"/>
  <polygon points="58,711 104,711 127,752 104,793 58,793 35,752" fill="var(--gold-light)"/>
  <polygon points="524,769 556,769 572,812 556,855 524,855 508,812" fill="var(--gold-light)"/>
</svg>

<div class="module" style="left:117px;top:226px">
  <svg width="191" height="166" viewBox="0 0 191 166" aria-hidden="true"><polygon points="48,0 143,0 191,83 143,166 48,166 0,83" fill="var(--gold)"/><polygon points="51,5 140,5 168,54 23,54" fill="var(--white)"/></svg>
  <div class="module-icon" style="background:var(--icon-a)" role="img" aria-label="Icono del módulo de contabilidad"></div>
  <div class="module-title">CONTABILIDAD</div>
  <p class="module-text">Es un software intuitivo que facilita el registro y tratamiento de todas las transacciones financieras.</p>
</div>

<div class="module" style="left:607px;top:136px">
  <svg width="191" height="166" viewBox="0 0 191 166" aria-hidden="true"><polygon points="48,0 143,0 191,83 143,166 48,166 0,83" fill="var(--gold)"/><polygon points="51,5 140,5 168,54 23,54" fill="var(--white)"/></svg>
  <div class="module-icon" style="background:var(--icon-c)" role="img" aria-label="Icono del módulo de compras"></div>
  <div class="module-title">COMPRAS</div>
  <p class="module-text long">Gestione sus cuentas actuales, agregar clientes nuevos o reciba candidatos convertidos. Enlace cuentas particulares con los productos o servicios que ofrece y monitoreé los ingresos generados por cada cuenta.</p>
</div>

<div class="module" style="left:445px;top:226px">
  <svg width="191" height="166" viewBox="0 0 191 166" aria-hidden="true"><polygon points="48,0 143,0 191,83 143,166 48,166 0,83" fill="var(--gold)"/><polygon points="51,5 140,5 168,54 23,54" fill="var(--white)"/></svg>
  <div class="module-icon" style="background:var(--icon-b)" role="img" aria-label="Icono del módulo de ventas"></div>
  <div class="module-title">VENTAS</div>
  <p class="module-text">Comprende todo el ciclo de gestión de ventas y facturación al permitirle realizar órdenes de venta, generar facturas y recibir pagos</p>
</div>

<div class="module" style="left:281px;top:318px">
  <svg width="191" height="166" viewBox="0 0 191 166" aria-hidden="true"><polygon points="48,0 143,0 191,83 143,166 48,166 0,83" fill="var(--gold)"/><polygon points="51,5 140,5 168,54 23,54" fill="var(--white)"/></svg>
  <div class="module-icon" style="background:var(--icon-d)" role="img" aria-label="Icono del módulo de bancos"></div>
  <div class="module-title" style="font-size:13px">BANCOS</div>
  <p class="module-text">Administre mejor los datos financieros por medio de la creación de mejores presupuestos, previsiones, planes a corto y largo plazo y mucho más.</p>
</div>

<div class="module" style="left:117px;top:408px">
  <svg width="191" height="166" viewBox="0 0 191 166" aria-hidden="true"><polygon points="48,0 143,0 191,83 143,166 48,166 0,83" fill="var(--gold)"/><polygon points="51,5 140,5 168,54 23,54" fill="var(--white)"/></svg>
  <div class="module-icon" style="background:var(--icon-e)" role="img" aria-label="Icono del módulo de presupuesto"></div>
  <div class="module-title">PRESUPUESTO</div>
  <p class="module-text">Este software es ideal para organizaciones pequeñas y medianas y ayuda a los equipos a reunir todos sus datos en un solo lugar.</p>
</div>

<div class="module" style="left:281px;top:502px">
  <svg width="191" height="166" viewBox="0 0 191 166" aria-hidden="true"><polygon points="48,0 143,0 191,83 143,166 48,166 0,83" fill="var(--gold)"/><polygon points="51,5 140,5 168,54 23,54" fill="var(--white)"/></svg>
  <div class="module-icon" style="background:var(--icon-f)" role="img" aria-label="Icono del módulo de inventarios"></div>
  <div class="module-title">INVENTARIOS</div>
  <p class="module-text">Administre almacenes, inventarios y la cantidad y valor de los artículos de manera mas eficiente.</p>
</div>

<div class="module" style="left:445px;top:594px">
  <svg width="191" height="166" viewBox="0 0 191 166" aria-hidden="true"><polygon points="48,0 143,0 191,83 143,166 48,166 0,83" fill="var(--gold)"/><polygon points="51,5 140,5 168,54 23,54" fill="var(--white)"/></svg>
  <div class="module-icon" style="background:var(--icon-g)" role="img" aria-label="Icono del módulo de nómina"></div>
  <div class="module-title">NÓMINA RH</div>
  <p class="module-text">Automatice los cálculos de la nómina para salarios, deducciones, impuestos y otras formas de compensación, en base a la legislación del país.</p>
</div>

<div class="module" style="left:281px;top:686px">
  <svg width="191" height="166" viewBox="0 0 191 166" aria-hidden="true"><polygon points="48,0 143,0 191,83 143,166 48,166 0,83" fill="var(--gold)"/><polygon points="51,5 140,5 168,54 23,54" fill="var(--white)"/></svg>
  <div class="module-icon" style="background:var(--icon-h)" role="img" aria-label="Icono del módulo CRM"></div>
  <div class="module-title big">CRM</div>
  <p class="module-text">Es una solución de gestión CRM con plataforma web e integración con ChatLink. Cotice desde NEXO con ChatLink</p>
</div>

<div class="module" style="left:607px;top:686px">
  <svg width="191" height="166" viewBox="0 0 191 166" aria-hidden="true"><polygon points="48,0 143,0 191,83 143,166 48,166 0,83" fill="var(--gold)"/><polygon points="51,5 140,5 168,54 23,54" fill="var(--white)"/></svg>
  <div class="module-icon" style="background:var(--icon-d)" role="img" aria-label="Icono del módulo de tareas"></div>
  <div class="module-title" style="font-size:13px">TAREAS</div>
  <p class="module-text long">Administre las tareas internas, externas y colaborar entre equipos de trabajo y sus cliente. Desde cualquiera de las aplicaciones, usted tiene acceso a potentes herramientas para ver el estado de sus tareas</p>
</div>

<div class="brand">
  <div class="brand-dot"></div>
  <div class="brand-name">Nexo<br>Cuentas</div>
</div>
</body>
</html>
```